New Word Template Design Project

Dellvane needs a modern and fresh corporate word template (*.dotm). We are a technology integrator the operates in the ICT sector in Portugal and Spain. Our solutions and services are detailed here: dellvane-example.com.
This word template should have mainly Dellvane's blue tones, and among other purposes, it's meant to be the basis of our commercial proposals. As such, in the cover page we need to place info such as: project name, client name, Dellvane reference, client reference, date and document type (the latter with less visual emphasis).
Our official font is Raleway and we are also sending our Brand Manual where the official company colors are specified.
Concerning the components of the document, we would like to have an index, 5 headings levels, 5 bullet points levels, 2 table styles and the other components that are part of the document we are also sending.

Target Market(s)

Executives and IT Directors

Industry/Entity Type

Information Technology

Font styles to use
Other font styles liked:
• Raleway

Colors
249fd3

Requirements
Must have
• Not jeopardizing the designers creativity, we would like it to be aligned with our website image.
• Respect brand colors (mostly the blue ones) and font
• Cover page info: project name, client name, Dellvane reference, client reference, date and document type
• 5 levels of headings considering a report
• 5 levels of bullet points
• 2 layouts for tables
• index
Nice to have
• A professional corporate template, yet conveying some modern, dynamic and "fresh" image.
Should not have
• Too many colors
• An unprofessional image

```html
<!DOCTYPE html>
<html lang="pt">
<head>
<meta charset="utf-8">
<title>Dellvane – Proposta</title>
<link rel="stylesheet" href="https://fonts.googleapis.com/css2?family=Raleway:wght@400;500;600;700&display=swap">
<style>
:root{
  --brand-blue:#249fd3;
  --ink:#231f20;
  --paper:#ffffff;
}
html,body{margin:0;padding:0;overflow:hidden;}
body{width:848px;height:1200px;background:var(--paper);font-family:"Raleway",sans-serif;color:var(--ink);position:relative;}
.brand{position:absolute;left:60px;top:40px;display:flex;align-items:center;gap:8px;}
.brand-mark{width:14px;height:14px;border-radius:50%;background:var(--brand-blue);}
.brand-name{font-size:17px;font-weight:500;color:var(--ink);}
.content{position:absolute;left:61px;top:176px;width:710px;font-size:13.4px;line-height:17px;}
h1{font-size:21px;font-weight:700;margin:0;line-height:24px;}
h2{font-size:15.5px;font-weight:700;margin:18px 0 0;line-height:19px;}
p{margin:0;}
ul{margin:0;padding-left:40px;list-style:none;}
li{position:relative;}
li::before{content:"";position:absolute;left:-20px;top:8px;width:3px;height:3px;border-radius:50%;background:var(--ink);}
.page-footer{position:absolute;left:61px;right:77px;top:1140px;display:flex;justify-content:space-between;font-weight:700;font-size:13px;}
.page-number{font-size:14px;}
</style>
</head>
<body>
<header class="brand">
  <span class="brand-mark"></span>
  <span class="brand-name">Dellvane</span>
</header>

<main class="content">
  <h1>TESTES</h1>
  <p>Engloba-se no âmbito destes serviços a realização de testes da solução, de forma a assegurar a qualidade global da mesma.</p>

  <h2>Documentação</h2>
  <ul>
    <li>Requisitos Técnicos - Detalhe dos requisitos para cada parametrização da solução;</li>
    <li>Cronograma de Projeto - Plano detalhado do projeto;</li>
    <li>Relatório de Projeto - Documento final do projeto com a descrição da solução implementada;</li>
    <li>Auto de Receção - Documento final de aceitação da solução por parte do cliente.</li>
  </ul>

  <h2>Prazos de Implementação</h2>
  <p>O início do projeto ocorrerá no mínimo 2 (duas) semanas após a adjudicação. Após a reunião de kick-off do projeto será apresentado um cronograma detalhado.</p>

  <h2>Exclusões</h2>
  <p>No âmbito dos serviços prestados estão excluídas as seguintes tarefas:</p>
  <ul>
    <li>Lorem ipsum dolor sit</li>
    <li>Lorem ipsum dolor sit amet</li>
    <li>Lorem ipsum dolor sit amet consectetur</li>
    <li>Lorem ipsum dolor sit</li>
    <li>Lorem ipsum dolor sit amet</li>
  </ul>

  <h2>Formação</h2>
  <p>A concretização de ações de formação constitui um elemento fundamental para o sucesso da solução, uma vez que é através da formação que os colaboradores irão adquirir o conhecimento e experiência necessários à operacionalização da solução.</p>
  <p>Considerando as características da solução proposta, preconiza-se o seguinte plano de formação:</p>
  <ul>
    <li>Lorem ipsum dolor s it</li>
    <li>Lorem ipsum dolor sit amet</li>
    <li>Lorem ipsum dolor sit amet consectetur</li>
  </ul>
</main>

<footer class="page-footer">
  <span class="page-number">02</span>
  <span class="page-url">www.dellvane-example.com</span>
</footer>
</body>
</html>
```